Flower delivery business needs sales brochure

I have a courier business that specialises in same-day flower deliveries; I want to make a single page A4 sales brochure (folded to DL) to give to our potential customers.
The company website is petalvanto.com, this will give an idea of who we are and what we do, as well as some graphics and colours that we use.
When opened, the inside A4 space of the brochure will be a pricelist, so the entire page will be an excel table with delivery locations and prices; we will add the prices ourselves later, so ideally the inside will be a background of some sort that won't obstruct text. Maybe light/transparent flowers and a background colour?
The front of the DL brochure should be mostly a title page, so business name, phone number, a graphic?
The first inside page should relate to our service, there's a lot of info on our website that you could use, so same day delivery, 10:30 and 2:30 pick-up times, established over 10 years ago, air-conditioned vans, delivery to 300+ suburbs.
The back page would be contact details and maybe a summary of the key points of the 'about us' section of the website.

Industry/Entity Type

Business

```html
<!DOCTYPE html>
<html lang="en">
<head>
<meta charset="utf-8">
<title>Petal Vanto – Brochure Presentation</title>
<link rel="stylesheet" href="https://fonts.googleapis.com/css2?family=Poiret+One&display=swap">
<style>
  :root {
    --board: #8a9e0d;
    --paper: #ffffff;
    --ink: #1d1d1d;
    --red: #f0353a;
    --leaf: #6f9c3a;
    --river: #0b5a2c;
    --orange: #d45a10;
    --yellow: #f7d22c;
    --mint: #93e2bd;
    --shadow: 4px 6px 10px rgba(0, 0, 0, 0.35);
  }
  * { box-sizing: border-box; margin: 0; padding: 0; }
  html, body { width: 1192px; height: 1200px; overflow: hidden; }
  body {
    background: var(--board);
    font-family: "Poiret One", sans-serif;
    color: var(--ink);
    position: relative;
  }
  .page {
    position: absolute;
    background: var(--paper);
    border: 1px solid #5b5b5b;
    box-shadow: var(--shadow);
    overflow: hidden;
  }
  .page--pricelist { left: 169px; top: 59px; width: 469px; height: 662px; }
  .page--services { left: 641px; top: 144px; width: 478px; height: 673px; }
  .page--back { left: 330px; top: 796px; width: 532px; height: 358px; }

  /* price list page */
  .daisy-field {
    position: absolute; inset: 0;
    background:
      radial-gradient(ellipse 110px 150px at 120px 130px, rgba(147,226,189,0.75), transparent 70%),
      radial-gradient(ellipse 120px 170px at 380px 220px, rgba(240,53,58,0.6), transparent 70%),
      radial-gradient(ellipse 90px 60px at 60px 200px, rgba(212,90,16,0.45), transparent 70%),
      radial-gradient(ellipse 230px 130px at 200px 560px, rgba(247,210,44,0.7), transparent 72%),
      radial-gradient(ellipse 110px 150px at 400px 470px, rgba(247,210,44,0.6), transparent 70%);
  }
  .map-area {
    position: absolute; left: 205px; top: 46px; width: 180px; height: 600px;
    background: radial-gradient(ellipse 50% 50% at 50% 50%, rgba(11,90,44,0.28), rgba(11,90,44,0.08) 70%, transparent 100%);
  }
  .brand-tile {
    position: absolute; left: 385px; top: 2px; width: 83px; height: 79px;
    background: radial-gradient(circle at 50% 45%, var(--orange) 0 38%, #a5b83a 40%, var(--leaf) 75%);
  }
  .brand-tile__name {
    position: absolute; left: 385px; top: 88px; width: 83px;
    text-align: center; font-size: 11px; color: var(--leaf); letter-spacing: 0.5px;
  }
  .brand-tile__url {
    position: absolute; left: 385px; top: 103px; width: 83px;
    text-align: center; font-size: 5px; color: var(--leaf);
  }
  .area-title { position: absolute; left: 31px; top: 352px; font-size: 14px; font-weight: 400; letter-spacing: -0.2px; }
  .area-note {
    position: absolute; left: 31px; top: 376px; width: 196px;
    font-size: 8px; line-height: 13px;
  }
  .order-call { position: absolute; left: 31px; top: 465px; font-size: 13.5px; }

  /* services page */
  .services-title {
    position: absolute; top: 40px; left: 0; right: 0;
    text-align: center; color: var(--red); font-size: 30px; font-weight: 400;
  }
  .services-title .star { font-size: 18px; vertical-align: 5px; margin: 0 6px; }
  .service-list { list-style: none; position: absolute; left: 60px; top: 112px; width: 370px; }
  .service-list li {
    position: relative; padding-left: 30px; font-size: 21px; line-height: 21px;
    margin-bottom: 18px;
  }
  .service-list li::before {
    content: ""; position: absolute; left: 0; top: 5px; width: 12px; height: 12px;
    border-radius: 50%; background: var(--red); box-shadow: 0 0 0 2px rgba(240,53,58,0.35);
  }
  .bloom-cluster {
    position: absolute;
    background:
      radial-gradient(circle at 62% 30%, var(--orange) 0 16%, transparent 30%),
      radial-gradient(circle at 78% 62%, var(--yellow) 0 12%, transparent 24%),
      radial-gradient(circle at 36% 60%, var(--red) 0 22%, transparent 36%);
  }
  .page--services .bloom-cluster { left: 18px; top: 500px; width: 190px; height: 170px; }
  .page--back .bloom-cluster { left: 20px; top: 165px; width: 210px; height: 190px; }

  .signoff { position: absolute; text-align: center; }
  .signoff__name { font-size: 38px; color: var(--leaf); line-height: 1; }
  .signoff__tag { font-size: 14px; color: var(--red); margin-top: 2px; }
  .signoff__url { font-size: 12px; color: var(--leaf); margin-top: 6px; }
  .page--services .signoff { left: 250px; top: 575px; width: 210px; }
  .page--services .signoff__name { font-size: 34px; }
  .page--back .signoff { left: 282px; top: 234px; width: 228px; }
</style>
</head>
<body>

<section class="page page--pricelist">
  <div class="daisy-field" role="img" aria-label="Scattered illustrated gerbera daisies in mint, red, orange and yellow"></div>
  <div class="map-area" role="img" aria-label="Illustrated map of the river through the metropolitan delivery area"></div>
  <div class="brand-tile" role="img" aria-label="Orange gerbera flower photograph on green"></div>
  <div class="brand-tile__name">PETAL VANTO</div>
  <div class="brand-tile__url">www.petalvanto.com</div>

  <h2 class="area-title">BRISBANE METROPOLITAN AREA</h2>
  <p class="area-note">All price lists are customized for each customer based on location of pickup and volume per week. Please contact us and we will be happy to provide a price list based on the information you provide.</p>
  <p class="order-call">call 0400 555 019 for your order!</p>
</section>

<section class="page page--services">
  <h2 class="services-title"><span class="star">&#10033;</span>SERVICES<span class="star">&#10033;</span></h2>
  <ul class="service-list">
    <li>Same day delivery</li>
    <li>Dedicated delivery vans for fresh flowers at your doorsteps</li>
    <li>More than 300 suburbs &nbsp;in Brisbane</li>
    <li>More than 10 years of &nbsp;business</li>
    <li>Same day courier service for florists, retailers &amp; wholesalers.</li>
  </ul>
  <div class="bloom-cluster" role="img" aria-label="Cluster of red, orange and yellow gerbera illustrations"></div>
  <div class="signoff">
    <div class="signoff__name">petal vanto</div>
    <div class="signoff__tag">Florist Delivery Service</div>
    <div class="signoff__url">www.petalvanto.com</div>
  </div>
</section>

<section class="page page--back">
  <div class="bloom-cluster" role="img" aria-label="Cluster of red, orange and yellow gerbera illustrations"></div>
  <div class="signoff">
    <div class="signoff__name">petal vanto</div>
    <div class="signoff__tag">Florist Delivery Service</div>
    <div class="signoff__url">www.petalvanto.com</div>
  </div>
</section>

</body>
</html>
```